Business card

We are looking for a creative person to deigns our company business card.

Target Market(s)

College age student

Industry/Entity Type

Accommodation

Contact Information for Business Card

We want a fun, clean and sophisticated design. It should look good, but more importantly the information should be legible.

Font styles to use
Serif
Sans Serif
Other font styles liked:
• Open Sans ,

Colors
33a6d7

Requirements
Must have
• Must have a young and memorable message. Be legible.
• Our logo on the back on a solid blue , please find color and logo attached
• LodgeBridgely.net on the back.
Nice to have
• I would like to have couple of different fonts on the LodgeBridgely.net on the back of the cards with a solid blue.

```html
<!DOCTYPE html>
<html lang="en">
<head>
<meta charset="utf-8">
<title>LodgeBridgely Business Card</title>
<link rel="stylesheet" href="https://fonts.googleapis.com/css2?family=Cinzel:wght@400&family=Open+Sans:wght@300;400;700&display=swap">
<style>
  :root {
    --brand-blue: #33a6d7;
    --deep-blue: #0c5d8e;
    --navy: #123a5c;
    --ink-blue: #1b7fc0;
    --paper: #f7f7f5;
    --backdrop: #e6e9ec;
    --white: #ffffff;
  }
  * { margin: 0; padding: 0; box-sizing: border-box; }
  html, body { width: 1200px; height: 800px; overflow: hidden; }
  body {
    background: var(--backdrop);
    font-family: "Open Sans", Arial, sans-serif;
    display: flex;
    align-items: center;
    justify-content: center;
    gap: 40px;
  }
  .card {
    width: 560px;
    height: 320px;
    position: relative;
    overflow: hidden;
    box-shadow: 0 6px 18px rgba(0,0,0,0.18);
  }

  /* Front */
  .card-front { background: var(--paper); }
  .front-top-band {
    position: absolute; top: 0; left: 0; right: 0;
    height: 14px; background: var(--deep-blue);
  }
  .front-bottom-band {
    position: absolute; bottom: 0; left: 0; right: 0;
    height: 30px; background: var(--brand-blue);
    display: flex; align-items: center; justify-content: center;
  }
  .address {
    color: var(--white); font-size: 9.5px; letter-spacing: 0.2px;
  }
  .brand-mark {
    position: absolute; left: 34px; top: 150px;
    display: flex; align-items: center; gap: 8px;
  }
  .brand-square {
    width: 22px; height: 22px; background: var(--brand-blue);
  }
  .brand-name {
    font-weight: 700; font-size: 22px; color: var(--deep-blue);
    letter-spacing: -0.3px;
  }
  .contact-block {
    position: absolute; left: 258px; top: 58px;
  }
  .person-name {
    font-family: "Cinzel", Georgia, serif;
    font-size: 30px; color: var(--navy); letter-spacing: 1px;
    margin-bottom: 24px;
  }
  .contact-list { list-style: none; }
  .contact-item {
    display: flex; align-items: center; gap: 12px;
    font-size: 14.5px; color: var(--ink-blue);
    margin-bottom: 7px; margin-left: 14px;
  }
  .contact-icon { width: 13px; height: 13px; fill: var(--navy); flex: none; }

  /* Back */
  .card-back {
    background: var(--brand-blue);
    display: flex; flex-direction: column; align-items: center; justify-content: center;
    gap: 26px;
  }
  .back-mark { display: flex; align-items: center; gap: 10px; }
  .back-mark .brand-square { width: 28px; height: 28px; background: var(--deep-blue); }
  .back-mark .brand-name { font-size: 34px; color: var(--deep-blue); }
  .back-url {
    font-weight: 300; font-size: 26px; color: var(--white); letter-spacing: 0.5px;
  }
</style>
</head>
<body>
  <section class="card card-front">
    <div class="front-top-band"></div>

    <div class="brand-mark">
      <span class="brand-square"></span>
      <span class="brand-name">LodgeBridgely</span>
    </div>

    <div class="contact-block">
      <h1 class="person-name">Marcus Hale</h1>
      <ul class="contact-list">
        <li class="contact-item">
          <svg class="contact-icon" viewBox="0 0 16 16" aria-hidden="true"><rect x="4" y="1" width="8" height="4"/><rect x="1" y="6" width="14" height="6" rx="1"/><rect x="4" y="10" width="8" height="5"/></svg>
          <span>555-014-2270</span>
        </li>
        <li class="contact-item">
          <svg class="contact-icon" viewBox="0 0 16 16" aria-hidden="true"><path d="M3 1l3 3-2 2c1 2 3 4 6 6l2-2 3 3-2 2C7 15 1 9 1 3z"/></svg>
          <span>555-014-2270</span>
        </li>
        <li class="contact-item">
          <svg class="contact-icon" viewBox="0 0 16 16" aria-hidden="true"><path d="M1 3h14v1L8 9 1 4z"/><path d="M1 6l7 5 7-5v7H1z"/></svg>
          <span>marcus@lodgebridgely.net</span>
        </li>
        <li class="contact-item">
          <svg class="contact-icon" viewBox="0 0 16 16" aria-hidden="true"><circle cx="8" cy="8" r="7"/><path d="M1 8h14M8 1c-3 4-3 10 0 14M8 1c3 4 3 10 0 14" stroke="#f7f7f5" stroke-width="1" fill="none"/></svg>
          <span>LodgeBridgely.net</span>
        </li>
      </ul>
    </div>

    <div class="front-bottom-band">
      <p class="address">88 Fernwood Rd., Suite 210, Portland, Oregon OR 97205</p>
    </div>
  </section>

  <section class="card card-back">
    <div class="back-mark">
      <span class="brand-square"></span>
      <span class="brand-name">LodgeBridgely</span>
    </div>
    <p class="back-url">LodgeBridgely.net</p>
  </section>
</body>
</html>
```